Nolvik Imaging Center web design and code

We need a new website for a Diagnostic Imaging Center in Fort Lauderdale, Florida.
The center has new RO advanced diagnostic equipment including a 3.0 Tesla MRI, a 128 slice PET/CT and a Varen T4 Ultrasound. Our facility has just been renovated and we have a lot of images, both facility and modality to use.
We have two client types, doctors who send their patients to our clinical Nolvik Center division, and clients who self-refer for screening studies to our Wellspire division. Both logos are attached. Please use the colors in the logos for the layout. Site should be coded in conventional HTML with CSS, but support multiple devices.
Updates

Reason: Waiting for additional designs. Most of the current designs are very similar in their structure and we would like more variety in terms of layout.

Target Market(s)

Doctors who refer patients for MRI, CT, PET, Bone Density and Ultrasound scans,
and
Retail clients who want full-body screening using MRI.

Industry/Entity Type

Medical Imaging

Coding

Coded - Design and coding required

Number of Pages Required

5+ page

Font styles to use
Sans Serif
Other font styles liked:
• Arquitecta

Requirements
Must have
• A good balance between color, shape, message and people/machine images.
• Must have images of the various machines, (RO Quillmark TN480, RO Quillmark 370, RO Varen T4) happy patients, clinical people, facility images and information about scans, preparations, costs, insurances we take.
• Must have links for social media and dynamic imagery.
Nice to have
• Some interactivity would be nice, including contact forms and scheduling application, Location map, directions, downloadable forms, history.
Should not have
• We do not want this to be built on WordPress platform. Should not be bound to a database platform that is proprietary or difficult to move.

```html
<!DOCTYPE html>
<html lang="en">
<head>
<meta charset="utf-8">
<title>Nolvik Imaging Center</title>
<link rel="stylesheet" href="https://fonts.googleapis.com/css2?family=Open+Sans:wght@400;600;700;800&display=swap">
<style>
:root{
  --green:#7dc242;
  --green-dark:#5f9e2c;
  --charcoal:#333333;
  --text:#555555;
  --muted:#888888;
  --band:#ececec;
  --footer:#2b2b2b;
  --footer-bottom:#1e1e1e;
  --white:#ffffff;
  --line:#dddddd;
}
*{box-sizing:border-box;margin:0;padding:0}
html,body{width:1200px;height:2184px;overflow:hidden}
body{font-family:'Open Sans',Arial,sans-serif;color:var(--text);background:var(--white);position:relative}
.abs{position:absolute}

/* header */
.site-header{top:0;left:0;width:1200px;height:120px;background:var(--white)}
.brand{left:72px;top:44px;display:flex;align-items:center;gap:12px}
.brand-mark{width:22px;height:22px;background:var(--green)}
.brand-name{font-weight:600;font-size:28px;line-height:32px;color:var(--charcoal)}
.header-call{right:70px;top:40px;display:flex;align-items:center;gap:12px;font-size:19px;color:var(--charcoal);font-weight:600}
.call-icon{width:40px;height:40px;border-radius:50%;background:var(--charcoal);display:flex;align-items:center;justify-content:center}

.main-nav{top:120px;left:0;width:1200px;height:40px;background:var(--green)}
.main-nav ul{list-style:none;display:flex;margin-left:70px;height:40px}
.main-nav li{font-size:14px;font-weight:700;color:var(--white);padding:0 22px;line-height:40px;text-transform:uppercase}
.main-nav li.active{background:var(--charcoal)}

/* hero */
.hero{top:160px;left:0;width:1200px;height:500px;background:linear-gradient(100deg,#9fb4c4 0%,#dfe8ee 40%,#f3f6f8 60%,#c9d4dc 100%)}
.hero-flags{left:72px;top:60px;display:flex;gap:6px}
.hero-flags span{width:22px;height:14px;background:#c9c9c9}
.hero-title{left:72px;top:125px;width:560px;font-size:40px;line-height:46px;font-weight:800;color:var(--white);text-transform:uppercase;text-shadow:0 2px 6px rgba(0,0,0,.35)}
.hero-dots{left:530px;top:450px;display:flex;gap:12px}
.hero-dots span{width:22px;height:22px;border-radius:50%;background:var(--green)}
.hero-dots span.on{background:var(--white)}

/* modalities */
.modalities{top:660px;left:0;width:1200px;height:405px;background:var(--band)}
.modality{top:52px;width:310px}
.modality-photo{height:164px;background:linear-gradient(180deg,#d6dde2,#aeb9c1)}
.modality-body{height:164px;background:var(--green);color:var(--white);text-align:center;padding:16px 22px}
.modality-body h3{font-size:26px;font-weight:700;margin-bottom:8px}
.modality-body p{font-size:13px;line-height:18px}

/* scheduling */
.schedule{top:1120px;left:72px;width:600px}
.tabs{display:flex;gap:6px}
.tab{font-size:14px;padding:8px 22px;background:var(--charcoal);color:var(--white)}
.tab.alt{background:var(--green)}
.schedule-box{border:1px solid var(--line);padding:26px 24px;height:300px;box-shadow:0 2px 6px rgba(0,0,0,.08)}
.schedule-box h2{font-size:20px;font-weight:600;color:var(--charcoal);text-transform:uppercase;margin-bottom:14px}
.schedule-box p{font-size:13px;line-height:19px;margin-bottom:14px}
.btn{display:inline-block;background:var(--green);color:var(--white);font-size:22px;padding:10px 24px;font-weight:600}

.location{top:1150px;left:760px;width:372px}
.location h2{font-size:26px;font-weight:400;color:var(--charcoal);text-transform:uppercase;margin-bottom:16px}
.map{height:235px;background:linear-gradient(135deg,#e9e4d4,#d9e2cc 50%,#d3dbe3);border:1px solid var(--line)}

/* contact */
.contact{top:1480px;left:0;width:1200px;height:340px;background:linear-gradient(90deg,#cfd6db 0%,#e9edef 35%,#f6f7f8 60%,#eef1f3 100%)}
.contact-form{top:0;left:140px;width:380px;height:340px;background:var(--green);padding:18px 30px}
.contact-form h2{font-size:26px;color:var(--white);font-weight:600;text-transform:uppercase;margin-bottom:14px}
.field{background:var(--white);height:34px;margin-bottom:14px;font-size:13px;color:var(--muted);padding:8px 10px;width:270px}
.field.area{height:50px}
.submit{display:inline-block;background:var(--charcoal);color:var(--white);font-size:14px;font-weight:700;padding:8px 22px}
.why{top:18px;left:570px;width:560px}
.why h2{font-size:21px;font-weight:700;color:var(--charcoal);margin-bottom:14px}
.why ul{list-style:none}
.why li{display:flex;gap:10px;font-size:13px;line-height:18px;margin-bottom:9px;color:var(--text)}
.why svg{flex:none;margin-top:3px}

/* footer */
.site-footer{top:1860px;left:0;width:1200px;height:280px;background:var(--footer);color:#bbbbbb}
.foot-col{top:30px}
.foot-col h4{font-size:20px;font-weight:400;color:var(--white);margin-bottom:14px}
.foot-col p,.foot-col li{font-size:13px;line-height:20px}
.foot-col ul{list-style:none}
.foot-col a{color:var(--green);text-decoration:none}
.sub-row{display:flex;margin-top:14px}
.sub-input{width:200px;height:30px;background:var(--white)}
.sub-btn{background:var(--green);color:var(--white);font-size:13px;padding:5px 12px}
.socials{left:150px;top:240px;display:flex;gap:8px}
.socials span{width:26px;height:26px;border-radius:50%;background:#777777}
.foot-bottom{top:2140px;left:0;width:1200px;height:44px;background:var(--footer-bottom);color:#999999;font-size:12px;line-height:44px;text-align:right;padding-right:70px}
</style>
</head>
<body>

<header class="site-header abs">
  <div class="brand abs">
    <span class="brand-mark"></span>
    <span class="brand-name">Nolvik Imaging Center</span>
  </div>
  <div class="header-call abs">
    <span class="call-icon"><svg width="20" height="20" viewBox="0 0 24 24"><path fill="#fff" d="M6.6 10.8a15 15 0 0 0 6.6 6.6l2.2-2.2c.3-.3.7-.4 1-.2 1.1.4 2.3.6 3.6.6.6 0 1 .4 1 1V20c0 .6-.4 1-1 1A17 17 0 0 1 3 4c0-.6.4-1 1-1h3.5c.6 0 1 .4 1 1 0 1.3.2 2.5.6 3.6.1.3 0 .7-.2 1z"/></svg></span>
    Call Us | 08 5550 1482
  </div>
</header>

<nav class="main-nav abs">
  <ul>
    <li class="active">Home</li><li>Departments</li><li>Doctors</li><li>Services</li><li>News</li><li>Audio</li><li>Gallery</li><li>Contact</li>
  </ul>
</nav>

<section class="hero abs" role="img" aria-label="Photo of a modern MRI scanner in a bright scanning room">
  <div class="hero-flags abs"><span></span><span></span></div>
  <h1 class="hero-title abs">Most advanced technology of its kind in the world has arrived!</h1>
  <div class="hero-dots abs"><span class="on"></span><span></span><span></span><span></span></div>
</section>

<section class="modalities abs">
  <article class="modality abs" style="left:72px">
    <div class="modality-photo" role="img" aria-label="Photo of the MRI scanner"></div>
    <div class="modality-body"><h3>MRI</h3><p>Lorem ipsum dolor sit amet, consectetur adipiscing elit, sed do eiusmod tempor incididunt ut labore et dolore magna aliqua. Ut enim ad.</p></div>
  </article>
  <article class="modality abs" style="left:448px">
    <div class="modality-photo" role="img" aria-label="Photo of the CT scanner"></div>
    <div class="modality-body"><h3>CT</h3><p>Lorem ipsum dolor sit amet, consectetur adipiscing elit, sed do eiusmod tempor incididunt ut labore et dolore magna aliqua. Ut enim ad.</p></div>
  </article>
  <article class="modality abs" style="left:828px">
    <div class="modality-photo" role="img" aria-label="Photo of the PET scanner"></div>
    <div class="modality-body"><h3>PET</h3><p>Lorem ipsum dolor sit amet, consectetur adipiscing elit, sed do eiusmod tempor incididunt ut labore et dolore magna aliqua. Ut enim ad.</p></div>
  </article>
</section>

<section class="schedule abs">
  <div class="tabs"><span class="tab">Scheduling</span><span class="tab alt">Download</span></div>
  <div class="schedule-box">
    <h2>Nolvik Imaging Center</h2>
    <p>Lorem ipsum dolor sit amet, consectetur adipiscing elit, sed do eiusmod tempor incididunt ut labore et dolore magna aliqua. Ut enim ad minim veniam, quis nostrud exercitation ullamco laboris nisi.</p>
    <p>Duis aute irure dolor in reprehenderit in voluptate velit esse cillum dolore eu fugiat nulla pariatur. Excepteur sint occaecat cupidatat non proident, sunt in culpa qui officia deserunt mollit anim.</p>
    <span class="btn">Scheduling Now</span>
  </div>
</section>

<section class="location abs">
  <h2>Location Map</h2>
  <div class="map" role="img" aria-label="Street map showing the center's location"></div>
</section>

<section class="contact abs" role="img" aria-label="Soft background photo of a scanning room">
  <form class="contact-form abs">
    <h2>Contact Form</h2>
    <div class="field">First Name</div>
    <div class="field">Last Name</div>
    <div class="field">Phone Number</div>
    <div class="field area">Comments</div>
    <span class="submit">SUBMIT</span>
  </form>
  <div class="why abs">
    <h2>Why Would You Send Your Patient Anywhere else</h2>
    <ul>
      <li><svg width="12" height="12" viewBox="0 0 12 12"><path d="M1 6l3 3 7-7" stroke="#5f9e2c" stroke-width="2" fill="none"/></svg>Lorem ipsum dolor sit amet, consectetur adipiscing elit, sed do eiusmod tempor.</li>
      <li><svg width="12" height="12" viewBox="0 0 12 12"><path d="M1 6l3 3 7-7" stroke="#5f9e2c" stroke-width="2" fill="none"/></svg>Tempor incididunt ut labore et dolore magna aliqua, ut enim ad minim.</li>
      <li><svg width="12" height="12" viewBox="0 0 12 12"><path d="M1 6l3 3 7-7" stroke="#5f9e2c" stroke-width="2" fill="none"/></svg>Quis nostrud exercitation ullamco laboris nisi ut aliquip ex ea commodo.</li>
      <li><svg width="12" height="12" viewBox="0 0 12 12"><path d="M1 6l3 3 7-7" stroke="#5f9e2c" stroke-width="2" fill="none"/></svg>Consequat duis aute irure dolor in reprehenderit in voluptate velit esse.</li>
      <li><svg width="12" height="12" viewBox="0 0 12 12"><path d="M1 6l3 3 7-7" stroke="#5f9e2c" stroke-width="2" fill="none"/></svg>Cillum dolore eu fugiat nulla pariatur, excepteur sint occaecat cupidatat.</li>
      <li><svg width="12" height="12" viewBox="0 0 12 12"><path d="M1 6l3 3 7-7" stroke="#5f9e2c" stroke-width="2" fill="none"/></svg>Non proident sunt in culpa qui officia deserunt mollit anim id est laborum.</li>
      <li><svg width="12" height="12" viewBox="0 0 12 12"><path d="M1 6l3 3 7-7" stroke="#5f9e2c" stroke-width="2" fill="none"/></svg>Sed ut perspiciatis unde omnis iste natus error sit voluptatem accusantium.</li>
      <li><svg width="12" height="12" viewBox="0 0 12 12"><path d="M1 6l3 3 7-7" stroke="#5f9e2c" stroke-width="2" fill="none"/></svg>Doloremque laudantium, totam rem aperiam eaque ipsa quae ab illo inventore.</li>
    </ul>
  </div>
</section>

<footer class="site-footer abs">
  <div class="foot-col abs" style="left:100px;width:220px">
    <h4>Contact</h4>
    <p>412 Harbor Reach Road, Suite 9,<br>Ashmere, FL 33301<br><a>Get Directions</a></p>
    <p style="margin-top:14px">Phone: 555-014-2290<br>Fax: 555-014-2291<br><a>Email Us</a></p>
  </div>
  <div class="foot-col abs" style="left:362px;width:200px">
    <h4>Our Features</h4>
    <ul><li>Home</li><li>Meet Our Staff</li><li>Patient Testimonials</li><li>Videos</li><li>Work Place Wellness</li><li>Contact</li></ul>
  </div>
  <div class="foot-col abs" style="left:582px;width:200px">
    <h4>Quick Links</h4>
    <ul><li>Home</li><li>Meet Our Staff</li><li>Patient Testimonials</li><li>Videos</li><li>Work Place Wellness</li><li>Contact</li></ul>
  </div>
  <div class="foot-col abs" style="left:790px;width:320px">
    <h4>Subscribe to Our NewsLetter</h4>
    <p>Get the latest offers &amp; prices directly in your mail box</p>
    <div class="sub-row"><span class="sub-input"></span><span class="sub-btn">Subscribe</span></div>
  </div>
  <div class="socials abs"><span></span><span></span><span></span><span></span><span></span></div>
</footer>
<div class="foot-bottom abs">Copyright © 2015 Nolvik Imaging Center. All rights reserved</div>

</body>
</html>
```